Veltrix 2 Specialist requires 3 Appealing Responsive Banners

For our website we need 3 appealing responsive banners which match the colors and style on our homepage. We do not just want static images we can place in our current slider, we require working html templates we can implement in our Veltrix 2 webshop directly. We are replacing the complete banner on the website.

This means you might need to add the javascript to properly make elements show and hide aswell as the Javascript to show the banners.

You can see the current banner on the homepage of https://www.plorvani.nl/

The random man with hands holding a web of information will be replaced with the banners you created, but we prefer that the background of the banner spans the whole page. The elements on top, you can decide for yourself it it looks nicer in your design to make it full width or stick to the content width of the content below.

These 3 banners we need will all click to landing pages on our website.

Requirements:
- The banners need to be responsive according to the Sparrow Scaffold CSS which is already in our website. Responsiveness just needs to be added in 2 degrees. Normal version and a mobile version. Tablets may show the normal version.
- The colors of the banners need to fit in our current website. The black, blue and orange colors are our main colors, but feel free to make it colorful.
- We dont want the Call to Action on each banner to be a button. The whole banner will be clickable, so the banner needs to reflect that.
- The banners need to be containing the specified key values for that banner which are specified for each banner below
- We do not like to use photos, but prefer a banner with created elements.

An example of what i mean with created elements is that of one of our competitors: https://www.quorbelo.com/

Responsiveness:
On mobile phones we'd like to show really simplified versions of the banners. Versions with just enough information to be informative and inviting to click through. On tablets we will just show the normal banner for now.

Banner 1: Single Sign-On
Will link to this page: https://www.plorvani.nl/veltrix-2-single-sign-on.html
Some keywords to spark your imagination: Central Login, Security, User Management, Corporate Identity Management
Key Feature 1: Needs to show that we integrate Identity Providers including Dunhale Cirrus, Dunhale KPTR, PellumVault, Yendi7, Brimzo and others.
Key Feature 2: It needs to visually suggest that identity management is the goal (could be like a user, a lock or maybe a finger print)

Banner 2: Webhooks
Will link to this page: https://www.plorvani.nl/veltrix-2-webhook-connector.html
Some Keywords to spark your imagination: Integration, Connect Veltrix 2 to any web interface, Automation, Analyzation.
Key Feature 1: Show Veltrix to be sending information to external services for Marketing purposes.
Key Feature 2: It needs to visually suggest that a connection is made between Veltrix and an external system
Key Feature 3: Must not be too abstract or customers will not see how they can use this extension in an actual case.

Banner 3: Veltrix Support
Will link to this page: https://www.plorvani.nl/veltrix-support.html
Some Keywords to spark your imagination: Resolve Issues, Performance Troubleshooting, Installation Service, Bugfixing, Upgrade Service
Key Feature 1: It needs to visually suggest we resolve their problems and help them grow their shop to higher levels
Key Feature 2: A sense of urgency may be added to the banner to show that we can help in matters of urgency.

In the end we require the created HTML/CSS/JS aswell as any of the used AI or PSD files so that we could create alternative banners with these banners if needed in the future.

Business to Large Businesses

Software Development

Coded - Design and coding required

1 page

Designer to choose colors to be used in the design.

• Scaffold 4 compatible banners

```html
<!DOCTYPE html>
<html lang="en">
<head>
<meta charset="utf-8">
<title>Veltrix 2 Single Sign-On Banner</title>
<link rel="stylesheet" href="https://fonts.googleapis.com/css2?family=Open+Sans:wght@300;400;700&display=swap">
<style>
  :root {
    --orange: #f26a1b;
    --orange-band: #f47c2c;
    --blue-deep: #0a2a6b;
    --blue-mid: #1560c4;
    --blue-bright: #5aa8f0;
    --blue-pale: #cfe6ff;
    --white: #ffffff;
    --divider: rgba(255, 255, 255, 0.5);
  }
  html, body {
    margin: 0;
    padding: 0;
    overflow: hidden;
    background: var(--white);
  }
  .banner {
    position: relative;
    display: block;
    width: 1200px;
    height: 366px;
    overflow: hidden;
    background: var(--orange);
    font-family: "Open Sans", Arial, sans-serif;
    color: var(--white);
    text-decoration: none;
  }
  .banner-shapes {
    position: absolute;
    inset: 0;
    width: 1200px;
    height: 366px;
  }
  .headline {
    position: absolute;
    left: 703px;
    top: 50px;
    margin: 0;
    font-size: 27px;
    line-height: 42px;
    letter-spacing: 0.3px;
    text-transform: uppercase;
  }
  .headline-light { display: block; font-weight: 300; }
  .headline-strong { display: block; font-weight: 700; }
  .provider-bar {
    position: absolute;
    left: 0;
    top: 288px;
    width: 1200px;
    height: 74px;
  }
  .provider {
    position: absolute;
    top: 12px;
    height: 50px;
    display: flex;
    align-items: center;
    justify-content: center;
    gap: 9px;
    font-size: 22px;
    font-weight: 400;
    color: var(--white);
    white-space: nowrap;
    box-sizing: border-box;
  }
  .provider + .provider { border-left: 1px dotted var(--divider); }
  .provider-mark {
    flex: none;
    width: 22px;
    height: 22px;
    background: var(--white);
  }
  .provider-mark.round { border-radius: 50%; }
  .provider-brimzo { left: 0; width: 218px; font-size: 30px; }
  .provider-yendi7 { left: 218px; width: 206px; font-weight: 700; }
  .provider-pellumvault { left: 424px; width: 294px; font-weight: 700; letter-spacing: 0.5px; }
  .provider-kptr { left: 718px; width: 208px; }
  .provider-cirrus { left: 926px; width: 254px; }
</style>
</head>
<body>
<a class="banner" href="https://www.plorvani.nl/veltrix-2-single-sign-on.html">
  <svg class="banner-shapes" viewBox="0 0 1200 366" aria-hidden="true">
    <defs>
      <linearGradient id="orangeGlow" x1="0" y1="0" x2="1" y2="1">
        <stop offset="0" stop-color="#f15f14"/>
        <stop offset="1" stop-color="#f88a3f"/>
      </linearGradient>
      <radialGradient id="fingerprintGlow" cx="0.36" cy="0.55" r="0.72">
        <stop offset="0" stop-color="var(--blue-pale)"/>
        <stop offset="0.25" stop-color="var(--blue-bright)"/>
        <stop offset="0.62" stop-color="var(--blue-mid)"/>
        <stop offset="1" stop-color="var(--blue-deep)"/>
      </radialGradient>
    </defs>
    <rect width="1200" height="366" fill="url(#orangeGlow)"/>
    <path d="M520 366 C760 300 980 250 1200 150 L1200 366 Z" fill="var(--orange-band)" opacity="0.55"/>
    <path d="M640 300 C820 250 1000 210 1200 110" fill="none" stroke="#ffffff" stroke-opacity="0.12"/>
    <path d="M660 310 C840 262 1020 226 1200 130" fill="none" stroke="#ffffff" stroke-opacity="0.1"/>
  </svg>
  <svg class="banner-shapes" viewBox="0 0 1200 366" role="img" aria-label="Glowing blue fingerprint resting on a circuit board">
    <path d="M0 0 L680 0 C640 95 600 190 520 240 C450 282 340 286 0 286 Z" fill="url(#fingerprintGlow)"/>
  </svg>
  <h1 class="headline">
    <span class="headline-light">Central login, security,</span>
    <span class="headline-light">user management,</span>
    <span class="headline-strong">Corporate identity</span>
    <span class="headline-strong">management</span>
  </h1>
  <div class="provider-bar">
    <span class="provider provider-brimzo">Brimzo</span>
    <span class="provider provider-yendi7"><span class="provider-mark round"></span>Yendi7</span>
    <span class="provider provider-pellumvault"><span class="provider-mark"></span>PELLUMVAULT</span>
    <span class="provider provider-kptr"><span class="provider-mark"></span>Dunhale KPTR</span>
    <span class="provider provider-cirrus"><span class="provider-mark"></span>Dunhale Cirrus</span>
  </div>
</a>
</body>
</html>
```